FinTech company looking to revamp and expand client-facing interface for our financial models

Halvern Quotient currently has a very simple website that allows clients to interact with our financial models. We are looking to completely redesign the current site and add several extra pages to provide extra functionality. We want the design to have a modern, slick feel, that will work on both a desktop or a tablet. It should be straightforward for clients to move between different pages at any time, and clear from the layout how to interact with the more advanced features. We have included screenshots of existing pages in the attached design brief, as well as sketches of the functionality required by the new pages, but can't provide a direct link to the current site.
Target Market(s)
Professional investors that will be paying to access the interface
Industry/Entity Type
Finance
Number of Pages Required
4 page
Colors
Designer to choose colors to be used in the design.
Look and feel
Each slider illustrates characteristics of the customer's brand and the style your logo design should communicate.

```html
<!DOCTYPE html>
<html lang="en">
<head>
<meta charset="utf-8">
<title>Halvern Quotient — Financial models for busy investors</title>
<link rel="stylesheet" href="https://fonts.googleapis.com/css2?family=Roboto:wght@300;400;500;700&display=swap">
<style>
:root{
  --hero-a:#171a55;
  --hero-b:#0f2842;
  --violet:#4628b4;
  --violet-btn:#4b2fc2;
  --line-violet:#7d66e6;
  --ink:#111827;
  --muted:#8a8f9c;
  --dark-band:#0c1b2b;
  --white:#ffffff;
}
*{box-sizing:border-box;margin:0;padding:0}
html,body{width:1200px;height:2795px;overflow:hidden}
body{font-family:'Roboto',sans-serif;color:var(--ink);background:var(--white);position:relative}
.btn{position:absolute;display:flex;align-items:center;justify-content:center;font-size:12px;font-weight:500;border-radius:3px;text-decoration:none}
.btn-solid{background:var(--violet-btn);color:var(--white);box-shadow:0 6px 14px rgba(75,47,194,.3)}
.btn-outline-light{border:1px solid var(--white);color:var(--white)}
.btn-white{background:var(--white);color:var(--violet-btn)}
.btn-outline-violet{border:1px solid var(--violet-btn);color:var(--violet-btn)}
.brand{position:absolute;font-size:14px;font-weight:500;letter-spacing:4.6px;text-transform:uppercase;white-space:nowrap}

/* hero */
.hero{position:absolute;left:0;top:0;width:1200px;height:700px;background:linear-gradient(160deg,var(--hero-a) 0%,#141f50 50%,var(--hero-b) 100%)}
.hero .brand{left:150px;top:60px;color:var(--white)}
.nav{position:absolute;top:60px;font-size:12px;color:#8b93b8}
.nav a{color:inherit;text-decoration:none;position:absolute;white-space:nowrap}
.nav a.active{color:var(--white)}
.hero h1{position:absolute;left:113px;top:268px;color:var(--white);font-size:41px;line-height:54px;font-weight:300}
.hero h1 strong{font-weight:700;display:block}
.hero .lede{position:absolute;left:113px;top:396px;width:380px;font-size:13.5px;line-height:17.5px;color:#8f95b5;font-weight:300}
.chart{position:absolute;left:0;top:0}
.tip{position:absolute;left:948px;top:176px;width:110px;height:32px;background:var(--white);border-radius:16px;font-size:11.5px;font-weight:500;display:flex;align-items:center;justify-content:center;color:var(--ink)}

/* features */
.feature{position:absolute;top:775px;width:280px;text-align:center}
.feature .icon{width:58px;height:58px;border-radius:50%;background:var(--white);box-shadow:0 6px 18px rgba(20,20,60,.09);margin:0 auto;display:flex;align-items:center;justify-content:center}
.feature h3{font-size:12px;font-weight:400;margin-top:29px}
.feature p{font-size:13.5px;line-height:17.5px;color:var(--muted);font-weight:300;margin-top:15px}

/* call band */
.band{position:absolute;left:0;top:1033px;width:1200px;height:360px;background:var(--violet);color:var(--white);text-align:center}
.band h2{position:absolute;left:0;width:1200px;top:82px;font-size:28px;line-height:34px;font-weight:300}
.band p{position:absolute;left:0;width:1200px;top:168px;font-size:13.5px;line-height:17.5px;font-weight:300;color:#ddd6ff}
.pill{position:absolute;top:252px;width:87px;height:33px;border-radius:17px;font-size:12px;font-weight:500;display:flex;align-items:center;justify-content:center}
.pill-white{background:var(--white);color:var(--violet)}
.pill-outline{border:1px solid #d9d2ff;color:var(--white)}

/* testimonials */
.quote{position:absolute;top:1468px;width:309px;height:216px;text-align:center}
.quote.raised{background:var(--white);box-shadow:0 8px 30px rgba(20,20,60,.08);border-radius:4px}
.avatar{width:58px;height:58px;border-radius:50%;margin:25px auto 0}
.quote h4{font-size:12px;font-weight:400;margin-top:21px}
.quote .role{font-size:9.5px;color:var(--muted);margin-top:7px}
.quote blockquote{font-size:13.5px;line-height:17.5px;margin-top:23px}

/* dark band */
.trial{position:absolute;left:0;top:1759px;width:1200px;height:242px;background:var(--dark-band)}
.trial h2{position:absolute;left:113px;top:98px;color:var(--white);font-size:28px;line-height:34px;font-weight:300}

/* pricing */
.plan{position:absolute;top:2076px;width:474px;height:428px;border-radius:4px}
.plan.starter{left:113px;background:var(--white);box-shadow:0 10px 40px rgba(20,20,60,.08)}
.plan.business{left:613px;background:var(--violet);color:var(--white);box-shadow:0 20px 40px rgba(70,40,180,.25)}
.plan h3{position:absolute;left:50px;top:52px;font-size:54px;font-weight:700;letter-spacing:-.5px}
.plan .price{position:absolute;right:50px;top:74px;font-size:15px;font-weight:700}
.plan .price small{font-size:9px;font-weight:400}
.plan .desc{position:absolute;left:50px;top:142px;width:340px;font-size:13.5px;line-height:17.5px;font-weight:300;color:var(--muted)}
.plan.business .desc{color:#d9d1ff}
.plan ul{list-style:none;position:absolute;top:212px;left:50px;width:380px}
.plan li{position:absolute;font-size:12px;display:flex;align-items:center;gap:13px;white-space:nowrap}
.plan li svg{flex:none}
.plan .cta{position:absolute;left:50px;top:345px;width:93px;height:33px}
.plan .more{position:absolute;left:168px;top:355px;font-size:11.5px;font-weight:500;color:var(--muted)}
.plan.business .more{color:var(--white)}

/* footer */
.footer .brand{left:113px;top:2656px;color:var(--ink)}
.copy{position:absolute;left:113px;top:2732px;font-size:11px;color:var(--muted)}
.foot-nav{position:absolute;top:2732px;font-size:11.5px;color:#555b6a}
.foot-nav a{position:absolute;color:inherit;text-decoration:none;white-space:nowrap}
.foot-nav a.active{color:var(--ink)}
</style>
</head>
<body>

<header class="hero">
  <div class="brand">Halvern Quotient</div>
  <nav class="nav">
    <a class="active" style="left:562px">Home</a>
    <a style="left:620px">About us</a>
    <a style="left:692px">Features</a>
    <a style="left:763px">Services</a>
    <a style="left:833px">Contact</a>
  </nav>
  <a class="btn btn-solid" style="left:900px;top:50px;width:88px;height:33px">Signup</a>
  <a class="btn btn-outline-light" style="left:1000px;top:50px;width:88px;height:33px">Login</a>

  <h1>Financial models<strong>For busy Investors</strong></h1>
  <p class="lede">Lorem ipsum dolor sit amet, consectetur adipiscing elit. Nunc vestibulum, elit eu posuere pretium, mi mauris placerat eros, id sodales felis dui et mauris. Fusce id bibendum nisl.</p>
  <a class="btn btn-solid" style="left:113px;top:473px;width:137px;height:41px">Get Started</a>

  <svg class="chart" width="1200" height="700" viewBox="0 0 1200 700" role="img" aria-label="Rising growth line chart">
    <defs>
      <linearGradient id="area" x1="0" y1="0" x2="0" y2="1">
        <stop offset="0" stop-color="#5a3fd0" stop-opacity=".35"/>
        <stop offset="1" stop-color="#5a3fd0" stop-opacity="0"/>
      </linearGradient>
    </defs>
    <path d="M612 318 C650 322 672 340 702 334 S762 306 792 316 S850 300 882 288 S934 276 960 262 S990 246 1003 236 L1003 545 L612 545 Z" fill="url(#area)"/>
    <path d="M612 318 C650 322 672 340 702 334 S762 306 792 316 S850 300 882 288 S934 276 960 262 S990 246 1003 236" fill="none" stroke="var(--line-violet)" stroke-width="1.8"/>
    <line x1="1003" y1="236" x2="1003" y2="545" stroke="#3f3a8a" stroke-width="1"/>
    <path d="M997 208 L1003 215 L1009 208 Z" fill="#fff"/>
    <circle cx="1003" cy="236" r="5.5" fill="#8a74f0" stroke="#fff" stroke-width="2"/>
  </svg>
  <div class="tip">67% Increase</div>
</header>

<section class="features">
  <div class="feature" style="left:126px">
    <div class="icon"><svg width="20" height="16" viewBox="0 0 20 16"><path d="M1 15 V10 L5 4 L9 8 L13 3 L19 11 V15 Z" fill="#4628b4"/><path d="M0 15.5 H20" stroke="#4628b4" stroke-width="1.2"/></svg></div>
    <h3>Lorem Ipsum Dolor</h3>
    <p>Lorem ipsum dolor sit amet, consectetur adipiscing elit. Nunc vestibulum, elit eu posuere pretium, mi mauris placerat eros, id sodales felis dui et mauris.</p>
  </div>
  <div class="feature" style="left:460px">
    <div class="icon"><svg width="20" height="16" viewBox="0 0 20 16"><path d="M1 1 V15 H19" fill="none" stroke="#4628b4" stroke-width="1.4"/><rect x="4" y="8" width="2.4" height="6" fill="#4628b4"/><rect x="8" y="4" width="2.4" height="10" fill="#4628b4"/><rect x="12" y="6" width="2.4" height="8" fill="#4628b4"/><rect x="16" y="3" width="2.4" height="11" fill="#4628b4"/></svg></div>
    <h3>Sed Nunc Mi</h3>
    <p>Sed nunc mi, egestas non efficitur in, hendrerit eget nunc. Maecenas ex erat, aliquet sit amet eros sit amet, eleifend euismod urna. Morbi convallis.</p>
  </div>
  <div class="feature" style="left:793px">
    <div class="icon"><svg width="20" height="20" viewBox="0 0 20 20"><path d="M9 2 A8 8 0 1 0 18 11 H9 Z" fill="#4628b4"/><path d="M11 0 A8 8 0 0 1 20 9 H11 Z" fill="#4628b4"/></svg></div>
    <h3>Nam Non Bibendum</h3>
    <p>Nam non bibendum nibh. Donec hendrerit laoreet dolor non sodales. Sed in metus et dolor bibendum euismod luctus ut elit. Nam sit amet justo lorem.</p>
  </div>
</section>

<section class="band">
  <h2>A lot of loren ipsum<br>&amp; investment data analysis</h2>
  <p>Lorem ipsum dolor sit amet, consectetur adipiscing elit. Nunc<br>vestibulum, elit eu posuere pretium, mi mauris placerat eros.</p>
  <a class="pill pill-white" style="left:507px">Signup</a>
  <a class="pill pill-outline" style="left:607px">Login</a>
</section>

<section class="testimonials">
  <figure class="quote" style="left:112px">
    <div class="avatar" role="img" aria-label="Portrait photo of Mara Lindqvist" style="background:radial-gradient(circle at 50% 45%,#c9856f,#8a3b2e)"></div>
    <h4>Mara Lindqvist</h4>
    <div class="role">CEO, Brightloop</div>
    <blockquote>“Lorem ipsum dolor sit amet, consectetur<br>adipiscing elit. Nunc vestibulum”</blockquote>
  </figure>
  <figure class="quote raised" style="left:445px">
    <div class="avatar" role="img" aria-label="Portrait photo of Peter Haldane" style="background:radial-gradient(circle at 50% 45%,#c9a48f,#5b5a5e)"></div>
    <h4>Peter Haldane</h4>
    <div class="role">Angel Investor</div>
    <blockquote>“Lorem ipsum dolor sit amet, consectetur<br>adipiscing elit. Nunc vestibulum”</blockquote>
  </figure>
  <figure class="quote" style="left:779px">
    <div class="avatar" role="img" aria-label="Portrait photo of Ivy Tanaka" style="background:radial-gradient(circle at 50% 45%,#d6a27c,#241613)"></div>
    <h4>Ivy Tanaka</h4>
    <div class="role">Financial Advisor</div>
    <blockquote>“Lorem ipsum dolor sit amet, consectetur<br>adipiscing elit. Nunc vestibulum”</blockquote>
  </figure>
</section>

<section class="trial">
  <h2>Try Halvern Quotient’s<br>predictive model today.</h2>
  <a class="btn btn-solid" style="left:779px;top:100px;width:142px;height:41px;box-shadow:none">Try for Free</a>
  <a class="btn btn-white" style="left:946px;top:100px;width:141px;height:41px">Subscribe Now</a>
</section>

<section class="pricing">
  <article class="plan starter">
    <h3>Starter</h3>
    <div class="price">£ 94.95 <small>/ mon</small></div>
    <p class="desc">Lorem ipsum dolor sit amet, consectetur adipiscing elit. Nunc vestibulum, elit eu posuere pretium, mi mauris placerat eros, id sodales felis.</p>
    <ul>
      <li style="left:0;top:0"><svg width="18" height="18" viewBox="0 0 18 18"><circle cx="9" cy="9" r="9" fill="#4628b4"/><path d="M5 9.2 L8 12 L13 6.5" fill="none" stroke="#fff" stroke-width="1.8"/></svg>Lorem ipsum list item</li>
      <li style="left:0;top:33px"><svg width="18" height="18" viewBox="0 0 18 18"><circle cx="9" cy="9" r="9" fill="#4628b4"/><path d="M5 9.2 L8 12 L13 6.5" fill="none" stroke="#fff" stroke-width="1.8"/></svg>100 List Items</li>
      <li style="left:0;top:65px"><svg width="18" height="18" viewBox="0 0 18 18"><circle cx="9" cy="9" r="9" fill="#4628b4"/><path d="M5 9.2 L8 12 L13 6.5" fill="none" stroke="#fff" stroke-width="1.8"/></svg>50 Lorem Item</li>
      <li style="left:213px;top:0"><svg width="18" height="18" viewBox="0 0 18 18"><circle cx="9" cy="9" r="9" fill="#c5c8d2"/><path d="M6 6 L12 12 M12 6 L6 12" stroke="#fff" stroke-width="1.8"/></svg>No list item</li>
      <li style="left:213px;top:33px"><svg width="18" height="18" viewBox="0 0 18 18"><circle cx="9" cy="9" r="9" fill="#c5c8d2"/><path d="M6 6 L12 12 M12 6 L6 12" stroke="#fff" stroke-width="1.8"/></svg>No list item</li>
      <li style="left:213px;top:65px"><svg width="18" height="18" viewBox="0 0 18 18"><circle cx="9" cy="9" r="9" fill="#c5c8d2"/><path d="M6 6 L12 12 M12 6 L6 12" stroke="#fff" stroke-width="1.8"/></svg>No list item</li>
    </ul>
    <a class="btn btn-solid cta">Get Started</a>
    <span class="more">Contact us for more details</span>
  </article>

  <article class="plan business">
    <h3>Business</h3>
    <div class="price">£ 199.95 <small>/ mon</small></div>
    <p class="desc">Lorem ipsum dolor sit amet, consectetur adipiscing elit. Nunc vestibulum, elit eu posuere pretium, mi mauris placerat eros, id sodales felis.</p>
    <ul>
      <li style="left:0;top:0"><svg width="18" height="18" viewBox="0 0 18 18"><circle cx="9" cy="9" r="9" fill="#fff"/><path d="M5 9.2 L8 12 L13 6.5" fill="none" stroke="#4628b4" stroke-width="1.8"/></svg>Lorem ipsum list item</li>
      <li style="left:0;top:33px"><svg width="18" height="18" viewBox="0 0 18 18"><circle cx="9" cy="9" r="9" fill="#fff"/><path d="M5 9.2 L8 12 L13 6.5" fill="none" stroke="#4628b4" stroke-width="1.8"/></svg>100 List Items</li>
      <li style="left:0;top:65px"><svg width="18" height="18" viewBox="0 0 18 18"><circle cx="9" cy="9" r="9" fill="#fff"/><path d="M5 9.2 L8 12 L13 6.5" fill="none" stroke="#4628b4" stroke-width="1.8"/></svg>50 Lorem Item</li>
      <li style="left:213px;top:0"><svg width="18" height="18" viewBox="0 0 18 18"><circle cx="9" cy="9" r="9" fill="#fff"/><path d="M5 9.2 L8 12 L13 6.5" fill="none" stroke="#4628b4" stroke-width="1.8"/></svg>List Item</li>
      <li style="left:213px;top:33px"><svg width="18" height="18" viewBox="0 0 18 18"><circle cx="9" cy="9" r="9" fill="#fff"/><path d="M5 9.2 L8 12 L13 6.5" fill="none" stroke="#4628b4" stroke-width="1.8"/></svg>Lorem Item</li>
      <li style="left:213px;top:65px"><svg width="18" height="18" viewBox="0 0 18 18"><circle cx="9" cy="9" r="9" fill="#fff"/><path d="M5 9.2 L8 12 L13 6.5" fill="none" stroke="#4628b4" stroke-width="1.8"/></svg>List Ipsum</li>
    </ul>
    <a class="btn btn-white cta">Get Started</a>
    <span class="more">Contact us for more details</span>
  </article>
</section>

<footer class="footer">
  <div class="brand">Halvern Quotient</div>
  <a class="btn btn-solid" style="left:900px;top:2646px;width:88px;height:33px">Signup</a>
  <a class="btn btn-outline-violet" style="left:1000px;top:2646px;width:88px;height:33px">Login</a>
  <div class="copy">© 2019, HalvernQuotient</div>
  <nav class="foot-nav">
    <a class="active" style="left:776px">Home</a>
    <a style="left:832px">About us</a>
    <a style="left:905px">Features</a>
    <a style="left:976px">Services</a>
    <a style="left:1046px">Contact</a>
  </nav>
</footer>

</body>
</html>
```